依頼詳細
購買意欲に響く電子チラシが欲しい。
記載項目
社名、情報、キャッチコピー
サイズ
A4
ページ数
片面
希望イメージ
シンプル 複雑
単色 カラフル
暗い 明るい
日常 高級
遊び心 厳粛
未来的 伝統的
女性的 男性的
希望する色
黄・オレンジ系、青系、無彩色系
納品ファイル
• 高解像度JPG (.jpg)
補足説明
販促用チラシの作成。

会員年齢層は平均40-50代が中心4000名ほど
見やすく、販促意欲を刺激するものを希望。

購入されたポイントは旅行やギフトを使えます。
会社ページ
https://www.lunafield-qz.app/

```html
<!DOCTYPE html>
<html lang="ja">
<head>
<meta charset="utf-8">
<title>1億円還元キャンペーン</title>
<link rel="stylesheet" href="https://fonts.googleapis.com/css2?family=Noto+Serif+JP:wght@500;700;900&family=Noto+Sans+JP:wght@400;700&display=swap">
<style>
  :root {
    --navy: #0f2340;
    --navy-deep: #0a1a31;
    --gold: #d8b56a;
    --gold-light: #f1dca2;
    --white: #ffffff;
    --red: #c8262b;
    --ink: #1b2b45;
    --band: #2a3950;
    --sky: #5c9fd8;
    --sea: #2aa6c2;
  }
  * { margin: 0; padding: 0; box-sizing: border-box; }
  html, body { width: 857px; height: 1200px; overflow: hidden; background: var(--navy); }
  .flyer { position: relative; width: 857px; height: 1200px; overflow: hidden; background: var(--navy); font-family: "Noto Serif JP", serif; color: var(--white); }

  .hero { position: absolute; left: 0; top: 0; width: 857px; height: 500px;
    background: linear-gradient(180deg, var(--sky) 0%, #8fc2ea 40%, var(--sea) 55%, #6fb5c4 75%, var(--navy) 100%); }

  .logo-box { position: absolute; right: 14px; top: 12px; width: 62px; height: 36px; border: 1px solid var(--white);
    font-family: "Noto Sans JP", sans-serif; font-size: 14px; display: flex; align-items: center; justify-content: center; }

  .cities { position: absolute; left: 36px; top: 60px; list-style: none; }
  .cities li { font-size: 30px; letter-spacing: 4px; line-height: 56px; font-weight: 500; text-shadow: 0 1px 4px rgba(0,0,0,.35); }

  .limited { position: absolute; left: 392px; top: 486px; width: 448px; height: 46px; background: var(--navy-deep);
    border: 2px solid var(--gold); color: var(--gold-light); font-weight: 900; font-size: 24px; letter-spacing: 2px;
    display: flex; align-items: center; justify-content: center; }

  .title { position: absolute; left: 0; right: 0; top: 546px; text-align: center; font-weight: 900; font-size: 54px; letter-spacing: 2px; line-height: 84px; }
  .title .amount { color: var(--gold); font-size: 68px; }
  .title .amount small { font-size: 40px; }

  .deadline { position: absolute; left: 40px; right: 40px; top: 636px; display: flex; align-items: center; gap: 18px;
    font-size: 18px; font-weight: 700; }
  .deadline::before, .deadline::after { content: ""; flex: 1; height: 1px; background: var(--gold); }

  .tiers { position: absolute; left: 24px; right: 24px; top: 676px; list-style: none; }
  .tier { height: 90px; display: flex; align-items: center; border-bottom: 1px dashed rgba(216,181,106,.55); }
  .tier-base { width: 260px; font-family: "Noto Sans JP", sans-serif; font-size: 13px; padding-left: 10px; }
  .tier-arrow { width: 16px; height: 20px; margin-right: 24px; flex: none; }
  .tier-rt { width: 230px; color: var(--gold); font-size: 54px; font-weight: 700; letter-spacing: 1px; white-space: nowrap; }
  .tier-rt small { font-size: 18px; margin-left: 2px; }
  .tier-bonus { width: 270px; height: 60px; background: linear-gradient(90deg, rgba(255,255,255,.75), #fff 15%, #fff 85%, rgba(255,255,255,.6));
    color: var(--ink); display: flex; flex-direction: column; align-items: center; justify-content: center; }
  .bonus-rate { font-family: "Noto Sans JP", sans-serif; font-size: 12px; }
  .bonus-rate b, .bonus-save b { color: var(--red); }
  .bonus-save { font-size: 14px; font-weight: 700; }
  .bonus-save b { font-size: 26px; font-weight: 900; }

  .closing { position: absolute; left: 0; right: 0; bottom: 0; height: 60px; background: var(--band);
    display: flex; align-items: center; justify-content: center; font-size: 20px; font-weight: 700; }
  .closing em { font-style: normal; color: var(--gold); font-size: 28px; margin: 0 4px; }
</style>
</head>
<body>
<div class="flyer">
  <div class="hero" role="img" aria-label="海辺の洞窟越しに見える青い空と海、白い砂浜の写真"></div>
  <div class="logo-box">ロゴ</div>
  <ul class="cities">
    <li>OKINAWA</li><li>TOKYO</li><li>OSAKA</li><li>KYOTO</li>
  </ul>

  <div class="limited">期間限定！RT 付与率 UP</div>

  <h1 class="title"><span class="amount">1億<small>円</small></span>還元キャンペーン</h1>
  <p class="deadline">2023 年 5 月 31 日（水）まで</p>

  <ul class="tiers">
    <li class="tier"><span class="tier-base">通常 25,000 円分 = 17.5RT</span>
      <svg class="tier-arrow" viewBox="0 0 16 20"><path d="M0 0 L16 10 L0 20Z" fill="#fff"/></svg>
      <span class="tier-rt">18.5<small>RT</small></span>
      <span class="tier-bonus"><span class="bonus-rate">付与率 <b>5%</b> UP</span><span class="bonus-save"><b>1,250</b>円お得</span></span></li>
    <li class="tier"><span class="tier-base">通常 50,000 円分 = 35RT</span>
      <svg class="tier-arrow" viewBox="0 0 16 20"><path d="M0 0 L16 10 L0 20Z" fill="#fff"/></svg>
      <span class="tier-rt">38.5<small>RT</small></span>
      <span class="tier-bonus"><span class="bonus-rate">付与率 <b>10%</b> UP</span><span class="bonus-save"><b>5,000</b>円お得</span></span></li>
    <li class="tier"><span class="tier-base">通常 100,000 円分 = 70RT</span>
      <svg class="tier-arrow" viewBox="0 0 16 20"><path d="M0 0 L16 10 L0 20Z" fill="#fff"/></svg>
      <span class="tier-rt">80.5<small>RT</small></span>
      <span class="tier-bonus"><span class="bonus-rate">付与率 <b>15%</b> UP</span><span class="bonus-save"><b>15,000</b>円お得</span></span></li>
    <li class="tier"><span class="tier-base">通常 200,000 円分 = 140RT</span>
      <svg class="tier-arrow" viewBox="0 0 16 20"><path d="M0 0 L16 10 L0 20Z" fill="#fff"/></svg>
      <span class="tier-rt">168<small>RT</small></span>
      <span class="tier-bonus"><span class="bonus-rate">付与率 <b>20%</b> UP</span><span class="bonus-save"><b>40,000</b>円お得</span></span></li>
    <li class="tier"><span class="tier-base">通常 500,000 円分 = 350RT</span>
      <svg class="tier-arrow" viewBox="0 0 16 20"><path d="M0 0 L16 10 L0 20Z" fill="#fff"/></svg>
      <span class="tier-rt">437.5<small>RT</small></span>
      <span class="tier-bonus"><span class="bonus-rate">付与率 <b>25%</b> UP</span><span class="bonus-save"><b>124,000</b>円お得</span></span></li>
  </ul>

  <p class="closing">確定した報酬から RT に変換すると通常より<em>断然お得</em>です</p>
</div>
</body>
</html>
```